Catholic composer needs poster for new musical, "THE STONE AND THE VIGIL, the Harvest Musical"

We need a dynamic poster for "The Stone and the Vigil," a new musical written for Catholic dinner theater. We need you to create an iconic design like you see in posters for classic musicals, like "Rosa Calendula," Lantern of the Harbour," or "Gilded." In our musical, “fire” represents the Holy Spirit, who showers man with his merciful love.

Miraculous events occur. A mighty wind from heaven fills the house. Tongues of fire appear over their heads. They speak in other tongues that are understandable by all present. They are emboldened to go out and tell the Good News to the world, despite the risks associated with evangelizing this fledgling religion. They exclaim, “Lord, you will show us the path to life.”

Target Market(s)

The audience is adult members of Catholic churches. But don't make the design look too "churchy."

Requirements
Must have
• Photoshop or Illustrated file with layers, or vector format.
Should not have
• Really don't want photos.

```html
<!DOCTYPE html>
<html lang="en">
<head>
<meta charset="utf-8">
<title>The Stone and the Vigil — The Harvest Musical</title>
<link rel="stylesheet" href="https://fonts.googleapis.com/css2?family=Anton&family=Oswald:wght@600&display=swap">
<style>
  :root {
    --paper: #ffffff;
    --ink: #141414;
  }
  html, body {
    margin: 0;
    padding: 0;
    width: 816px;
    height: 1200px;
    overflow: hidden;
    background: var(--paper);
  }
  .poster {
    display: block;
    width: 816px;
    height: 1200px;
    background: var(--paper);
  }
  .title-word {
    font-family: 'Anton', 'Impact', sans-serif;
    fill: var(--ink);
  }
  .tagline {
    font-family: 'Oswald', 'Arial Narrow', sans-serif;
    font-weight: 600;
    fill: var(--ink);
    font-size: 22px;
  }
  .subtitle {
    font-family: 'Anton', 'Impact', sans-serif;
    fill: var(--ink);
  }
  .credit {
    font-family: 'Anton', 'Impact', sans-serif;
    fill: var(--ink);
    font-size: 22px;
  }
  .detail-label {
    font-family: 'Anton', 'Impact', sans-serif;
    fill: var(--ink);
    font-size: 26px;
  }
  .website {
    font-family: 'Anton', 'Impact', sans-serif;
    fill: var(--ink);
  }
</style>
</head>
<body>
<svg class="poster" viewBox="0 0 816 1200" xmlns="http://www.w3.org/2000/svg" aria-label="The Stone and the Vigil, the Harvest Musical poster">
  <rect width="816" height="1200" fill="var(--paper)"/>

  <g class="main-title">
    <text class="title-word" x="50" y="245" font-size="236" textLength="718" lengthAdjust="spacingAndGlyphs">THE</text>
    <text class="title-word" x="50" y="484" font-size="236" textLength="718" lengthAdjust="spacingAndGlyphs">STONE</text>
    <text class="title-word" x="48" y="647" font-size="145" textLength="240" lengthAdjust="spacingAndGlyphs">AND</text>
    <text class="title-word" x="517" y="647" font-size="145" textLength="252" lengthAdjust="spacingAndGlyphs">THE</text>
    <text class="title-word" x="50" y="865" font-size="224" textLength="718" lengthAdjust="spacingAndGlyphs">VIGIL</text>
  </g>

  <g class="tagline-block">
    <text class="tagline" x="332" y="560" textLength="160" lengthAdjust="spacingAndGlyphs">"OH SPIRIT COME,</text>
    <text class="tagline" x="318" y="588" textLength="180" lengthAdjust="spacingAndGlyphs">YOU ARE MERCIFUL</text>
    <text class="tagline" x="332" y="616">LOVE"</text>
  </g>

  <text class="subtitle" x="50" y="920" font-size="54" textLength="718" lengthAdjust="spacingAndGlyphs">THE HARVEST MUSICAL</text>

  <g class="credits">
    <text class="credit" x="408" y="950" text-anchor="middle">A NEW MUSICAL FOR CATHOLIC DINNER THEATER</text>
    <text class="credit" x="408" y="977" text-anchor="middle">BY PAUL VERDEN</text>
  </g>

  <g class="event-details">
    <text class="detail-label" x="52" y="1042">WHERE:</text>
    <text class="detail-label" x="484" y="1042">TIME:</text>
    <text class="detail-label" x="52" y="1088">DATE:</text>
    <text class="detail-label" x="484" y="1088">PRICE:</text>
  </g>

  <text class="website" x="50" y="1180" font-size="56" textLength="718" lengthAdjust="spacingAndGlyphs">WWW.THESTONEANDTHEVIGIL.COM</text>
</svg>
</body>
</html>
```